Business card design for strategy and management consulting company. Would like to have a clean and professional business card, based on the attached logo. The company is a strategy and management consulting company focusing on sustainable business modlels based on economic, social and environmental market opportunities. Preferably the logo should be included on both sides of the design.

Industry/Entity Type

Business

Contact Information for Business Card

Håvard Lilleby, CEO/Management consultant
havard.lilleby@quarvenpartners.example
Mob: +47 948 26 317
Office: Vikfjell gate 14, pb 312 sentrum, N-0172 Oslo Norway

Requirements
Must have
• Include attached logo
Nice to have
• Would like to have the logo on both sides
Should not have
• Many colours.

```html
<!DOCTYPE html>
<html lang="en">
<head>
<meta charset="utf-8">
<title>Quarven business card</title>
<link href="https://fonts.googleapis.com/css2?family=Work+Sans:wght@400;600;700&display=swap" rel="stylesheet">
<style>
  :root {
    --backdrop: #2b2b2b;
    --card: #1e1e1e;
    --card-edge: #262626;
    --ink: #ffffff;
    --ink-soft: #d9d9d9;
    --accent: #f7e600;
  }
  html, body {
    margin: 0;
    padding: 0;
    width: 1200px;
    height: 900px;
    overflow: hidden;
    background: var(--backdrop);
    font-family: "Work Sans", Arial, sans-serif;
  }
  .canvas {
    position: relative;
    width: 1200px;
    height: 900px;
  }
  .card {
    position: absolute;
    left: 260px;
    width: 680px;
    height: 388px;
    background: var(--card);
    box-shadow: 0 10px 30px rgba(0,0,0,0.45);
    overflow: hidden;
  }
  .card--front { top: 46px; }
  .card--back { top: 466px; }

  .pattern-field {
    position: absolute;
    inset: 0;
    background: radial-gradient(ellipse at 75% 40%, #2c2c2c 0%, #1f1f1f 55%, #191919 100%);
  }

  .wordmark {
    position: absolute;
    display: flex;
    align-items: flex-start;
    gap: 8px;
    color: var(--ink);
    font-weight: 700;
    letter-spacing: -1px;
    line-height: 1;
  }
  .wordmark__dot {
    width: 14px;
    height: 14px;
    border-radius: 50%;
    background: var(--accent);
    margin-top: 4px;
  }
  .card--front .wordmark {
    font-size: 84px;
    left: 50%;
    top: 50%;
    transform: translate(-50%, -55%);
  }
  .card--back .wordmark {
    font-size: 62px;
    left: 48px;
    top: 150px;
  }

  .glow-field {
    position: absolute;
    left: 250px;
    top: 0;
    width: 230px;
    height: 388px;
    background: radial-gradient(ellipse at 50% 50%, #2e2e2e 0%, #232323 45%, rgba(30,30,30,0) 75%);
  }

  .divider {
    position: absolute;
    left: 332px;
    top: 108px;
    width: 2px;
    height: 170px;
    background: var(--ink-soft);
  }

  .contact {
    position: absolute;
    left: 356px;
    top: 104px;
    color: var(--ink-soft);
    font-size: 15px;
    line-height: 1.45;
  }
  .contact__name {
    margin: 0;
    color: var(--accent);
    font-size: 29px;
    font-weight: 600;
    line-height: 1.1;
  }
  .contact__role,
  .contact__address {
    margin: 0;
  }
  .contact__role { margin-bottom: 6px; }
  .contact__line {
    display: flex;
    align-items: center;
    gap: 9px;
    margin: 0;
  }
  .contact__line svg { flex: none; }
</style>
</head>
<body>
<div class="canvas">

  <section class="card card--front">
    <div class="pattern-field" role="img" aria-label="Subtle tonal tiled pattern covering the card front"></div>
    <div class="wordmark"><span>Quarven</span><span class="wordmark__dot"></span></div>
  </section>

  <section class="card card--back">
    <div class="glow-field" role="img" aria-label="Soft faint decorative glow behind the divider"></div>
    <div class="wordmark"><span>Quarven</span><span class="wordmark__dot"></span></div>
    <div class="divider"></div>
    <div class="contact">
      <p class="contact__name">Håvard Lilleby</p>
      <p class="contact__role">CEO/Management consultant</p>
      <p class="contact__address">Vikfjell gate 14,<br>pb 312 sentrum, N-0172 Oslo Norway</p>
      <p class="contact__line">
        <svg width="10" height="14" viewBox="0 0 10 14" aria-hidden="true">
          <rect x="1" y="1" width="8" height="12" rx="1.5" fill="none" stroke="#f7e600" stroke-width="1.5"/>
          <line x1="4" y1="10.5" x2="6" y2="10.5" stroke="#f7e600" stroke-width="1.5"/>
        </svg>
        <span>+47 948 26 317</span>
      </p>
      <p class="contact__line">
        <svg width="12" height="10" viewBox="0 0 12 10" aria-hidden="true">
          <rect x="0.75" y="0.75" width="10.5" height="8.5" fill="none" stroke="#f7e600" stroke-width="1.5"/>
          <polyline points="1,1 6,5.5 11,1" fill="none" stroke="#f7e600" stroke-width="1.3"/>
        </svg>
        <span>havard.lilleby@quarvenpartners.example</span>
      </p>
    </div>
  </section>

</div>
</body>
</html>
```